Web design for development company

We would like web, logo and business card designs for a construction and development company in Halifax, Nova Scotia called "R & M Group Developments Limited".

We would like the web design to be professional, and luxurious . The colours should be professional/more mature and easy to read. The website should include: home page, about page, projects, and contact.

The logo design should also be professional in appearance and minimal/not too busy with the company name included. I have attached a few logos that I like for inspiration.

We would like the cards to be double sided with one side being the logo and name of the company. The other side of the card should include the following: logo, company name, name, title, mobile number, office number, fax, email, and website link.

Target Market(s)

general public, potential clients/business partners

Industry/Entity Type

Construction and Development

Coding

Coded - Design and coding required

Number of Pages Required

5+ page

Font styles to use
Serif
Decorative

Requirements
Must have
• the website type i want to receive is coded (the uncoded won't correct to coded on the brief page for some reason) )
Should not have
• playful elements that make the website less professional.Unreadable logos and writing.

```html
<!DOCTYPE html>
<html lang="en">
<head>
<meta charset="utf-8">
<title>R &amp; M Group Developments Limited</title>
<link href="https://fonts.googleapis.com/css2?family=Poppins:wght@400;500;600;700&family=Lato:wght@400;700&display=swap" rel="stylesheet">
<style>
:root{
  --navy:#0c2a63;
  --navy-dark:#0a2456;
  --orange:#f26522;
  --orange-dark:#e2561a;
  --red:#d7262f;
  --text:#6d6d6d;
  --light:#f4f4f4;
  --line:#e6e6e6;
}
*{margin:0;padding:0;box-sizing:border-box}
html,body{width:1200px;height:3605px;overflow:hidden}
body{font-family:'Lato',sans-serif;color:var(--text);background:#fff;position:relative}
.abs{position:absolute}
.photo{position:absolute}

/* top bar */
.topbar{position:absolute;left:0;top:0;width:1200px;height:48px;background:#fff;border-bottom:1px solid var(--line);font-size:13px;color:#999}
.topbar .cell{position:absolute;top:0;height:48px;display:flex;align-items:center;gap:8px;border-left:1px solid var(--line);padding:0 26px}
.dot{width:10px;height:10px;border-radius:50%;background:#aaa;display:inline-block}
.topbar svg{width:12px;height:12px;fill:#999}

/* header */
.header{position:absolute;top:48px;left:0;width:1200px;height:98px;background:#fff}
.nav{position:absolute;top:62px;left:0;font-family:'Poppins',sans-serif;font-size:15px;color:#333}
.nav a{color:#333;text-decoration:none;position:absolute;white-space:nowrap}
.nav a.active{color:var(--orange)}
.brand-mark{position:absolute;left:561px;top:30px;width:78px;height:78px;border-radius:50%;background:var(--orange)}
.brand-name{position:absolute;left:0;width:1200px;text-align:center;top:110px;font-family:'Poppins',sans-serif;font-weight:600;font-size:15px;color:var(--navy)}

/* hero */
.hero{position:absolute;top:146px;left:0;width:1200px;height:640px;background:linear-gradient(100deg,#b9b2a2 0%,#8a8474 30%,#6a6456 55%,#4e4a42 80%,#3b3832 100%)}
.hero h1{position:absolute;left:602px;top:215px;font-family:'Poppins',sans-serif;font-weight:700;font-size:78px;color:#fff;line-height:1}
.hero h2{position:absolute;left:602px;top:305px;font-family:'Poppins',sans-serif;font-weight:400;font-style:italic;font-size:34px;color:#fff}
.hero p{position:absolute;left:604px;top:366px;width:480px;font-size:14px;line-height:30px;color:#fff;font-weight:700}
.btn{position:absolute;display:flex;align-items:center;justify-content:center;font-family:'Lato',sans-serif;font-weight:700;font-size:16px;text-transform:uppercase}
.btn-orange{background:var(--orange);color:#fff}
.btn-ghost{border:1px solid #fff;color:#fff}
.arrow-box{position:absolute;width:40px;height:40px;background:#fff;display:flex;align-items:center;justify-content:center}
.arrow-box svg{width:16px;height:16px;stroke:#333;fill:none;stroke-width:2}

.cta-band{position:absolute;top:786px;left:0;width:1200px;height:85px;background:linear-gradient(90deg,var(--orange-dark),var(--orange),#f47a3d)}
.cta-band p{position:absolute;left:146px;top:32px;color:#fff;font-weight:700;font-size:17px}
.btn-navy{background:var(--navy);color:#fff}

/* about */
.about-box{position:absolute;left:60px;top:927px;width:836px;height:435px;background:#fafafa}
.section-title{font-family:'Poppins',sans-serif;font-weight:600;color:var(--navy)}
.about-box h2{position:absolute;left:66px;top:76px;font-size:40px}
.about-box .rule{position:absolute;left:66px;top:132px;width:70px;height:3px;background:var(--red)}
.about-box p{position:absolute;left:66px;top:162px;width:470px;font-size:15px;line-height:30px}

/* projects */
.projects{position:absolute;top:1477px;left:0;width:1200px;height:742px;background:var(--navy)}
.projects .ghost{position:absolute;left:42px;top:54px;font-family:'Poppins',sans-serif;font-weight:700;font-size:108px;color:transparent;-webkit-text-stroke:1px rgba(255,255,255,.18);letter-spacing:2px}
.projects h2{position:absolute;left:110px;top:100px;font-family:'Poppins',sans-serif;font-weight:700;font-size:56px;color:#fff}
.card{position:absolute;top:192px;width:316px}
.card .photo{position:relative;width:316px;height:280px}
.card .cat{margin-top:14px;font-family:'Poppins',sans-serif;font-size:13px;font-weight:600;color:var(--orange);padding-left:2px}
.card h3{font-family:'Poppins',sans-serif;font-weight:500;font-size:16px;color:#fff;margin-top:2px;padding-left:2px}
.card p{font-size:13px;line-height:27px;color:#dde3ef;margin-top:10px;padding-left:2px;white-space:nowrap;overflow:hidden}
.card .find{margin-top:22px;margin-left:4px;width:156px;height:49px;border:1px solid #fff;color:#fff;display:flex;align-items:center;justify-content:center;font-family:'Poppins',sans-serif;font-size:15px;font-weight:500}

/* offer */
.offer h2{position:absolute;left:616px;top:2320px;font-family:'Poppins',sans-serif;font-weight:600;font-size:31px;color:var(--orange)}
.offer p{position:absolute;left:616px;width:428px;font-size:13px;line-height:22px}
.tab{position:absolute;left:1045px;top:2303px;width:155px;height:48px;border-left:4px solid #111;border-top:1px solid var(--line);border-bottom:1px solid var(--line);display:flex;align-items:center;justify-content:center;font-size:13px;color:#222;font-weight:700}
.arrow-line{border:1px solid #ccc}

/* testimonials */
.testi{position:absolute;top:2791px;left:0;width:1200px;height:471px;background:var(--light)}
.testi h2{position:absolute;width:1200px;text-align:center;top:54px;font-size:40px}
.quote{position:absolute;font-family:Georgia,serif;font-weight:700;font-size:230px;line-height:1;color:#c9c9c9}
.tcard{position:absolute;top:139px;width:429px;height:229px;padding:24px 22px}
.tcard.dark{background:var(--navy);color:#fff;box-shadow:0 4px 10px rgba(0,0,0,.25)}
.tcard.light{background:#fff;border:1px solid #999;border-bottom:3px solid var(--orange)}
.avatar{position:absolute;left:22px;top:24px;width:93px;height:83px;background:linear-gradient(135deg,#d8d4cf,#a89a8c)}
.tcard .name{position:absolute;left:130px;top:48px;font-family:'Poppins',sans-serif;font-size:16px;font-weight:500}
.tcard .role{position:absolute;left:132px;top:74px;font-size:13px}
.tcard p{position:absolute;left:22px;top:128px;width:395px;font-size:12px;line-height:27px}
.tcard.light .name{color:#333}
.tcard.light p,.tcard.light .role{color:#888}
.dots{position:absolute;left:550px;display:flex;gap:7px}
.dots span{width:14px;height:14px;border-radius:50%;border:1px solid #333}
.dots span.on{background:var(--orange);border-color:var(--orange)}
.testi .dots{top:405px}

/* footer */
.footer{position:absolute;top:3262px;left:0;width:1200px;height:284px;background:var(--navy-dark);color:#fff}
.footer h4{position:absolute;top:72px;font-family:'Poppins',sans-serif;font-weight:500;font-size:17px}
.footer h4.small{font-size:14px}
.footer .txt{position:absolute;font-size:12px;line-height:27px}
.footer .row{display:flex;align-items:center;gap:6px;height:32px;font-size:13px}
.footer svg{width:12px;height:12px;fill:#fff}
.map-area{position:absolute;left:883px;top:100px;width:200px;height:120px;background:linear-gradient(135deg,#1f5fb8,#123f86);border-radius:4px}
.copy{position:absolute;top:3546px;left:0;width:1200px;height:59px;background:var(--orange);color:#fff;text-align:center;line-height:59px;font-family:'Poppins',sans-serif;font-size:16px}
</style>
</head>
<body>

<div class="topbar">
  <div class="cell" style="left:112px"><span class="dot"></span><span class="dot"></span><span class="dot"></span><span class="dot"></span></div>
  <div class="cell" style="left:244px">
    <svg viewBox="0 0 12 12"><circle cx="6" cy="6" r="5" fill="none" stroke="#999" stroke-width="1.4"/><path d="M6 3v3.2l2 1.2" fill="none" stroke="#999" stroke-width="1.2"/></svg>
    Mon - Sat: 7:00 - 17:00
  </div>
  <div class="cell" style="left:452px;width:0;padding:0"></div>
  <div class="cell" style="left:717px">
    <svg viewBox="0 0 12 12"><path d="M2.5 1l2 .3.8 2.2-1.2 1a7 7 0 0 0 3.4 3.4l1-1.2 2.2.8.3 2c-.2.8-1 1.3-1.8 1.3A9 9 0 0 1 1 2.8C1 2 1.6 1.2 2.5 1z"/></svg>
    +1-902-555-0190
  </div>
  <div class="cell" style="left:889px">
    <svg viewBox="0 0 12 12"><rect x="1" y="2.5" width="10" height="7"/><path d="M1 2.5l5 4 5-4" stroke="#fff" fill="none"/></svg>
    info@rmgroupdev.ca
  </div>
  <div class="cell" style="left:1087px;width:0;padding:0"></div>
</div>

<div class="header"></div>
<svg class="abs" style="left:430px;top:20px" width="340" height="40" viewBox="0 0 340 40"><path d="M0 30 C80 30 110 0 170 0 C230 0 260 30 340 30 L340 40 L0 40Z" fill="#fff"/></svg>
<div class="brand-mark"></div>
<div class="brand-name">R &amp; M Group Developments Limited</div>
<nav class="nav">
  <a class="active" style="left:114px;top:47px">Home</a>
  <a style="left:193px;top:47px">About</a>
  <a style="left:275px;top:47px">Projects</a>
  <a style="left:368px;top:47px">Contact</a>
  <a style="left:768px;top:47px">
    <svg style="width:10px;height:12px;vertical-align:-1px" viewBox="0 0 10 12"><path d="M5 0a4 4 0 0 1 4 4c0 3-4 8-4 8S1 7 1 4a4 4 0 0 1 4-4z" fill="#333"/><circle cx="5" cy="4" r="1.5" fill="#fff"/></svg>
    48, Halifax, Nova Scotia</a>
  <a style="left:992px;top:47px">
    <svg style="width:11px;height:12px;vertical-align:-1px" viewBox="0 0 11 12"><circle cx="5.5" cy="3.3" r="3" fill="#333"/><path d="M0 12c0-4 2.5-5.5 5.5-5.5S11 8 11 12z" fill="#333"/></svg>
    Login</a>
  <a style="left:1075px;top:49px">
    <svg style="width:13px;height:13px" viewBox="0 0 13 13"><circle cx="5.5" cy="5.5" r="4" fill="none" stroke="#333" stroke-width="2"/><path d="M8.5 8.5L12 12" stroke="#333" stroke-width="2.2"/></svg>
  </a>
</nav>

<section class="hero" role="img" aria-label="Construction crew in safety vests and hard hats walking in front of a building under construction">
  <h1>R &amp; M Group</h1>
  <h2>Developments Limited</h2>
  <p>Lorem ipsum dolor sit amet, consectetur adipiscing elit, sed do eiusmod tempor incididunt ut labore et dolore magna aliqua.</p>
  <div class="btn btn-orange" style="left:604px;top:446px;width:154px;height:52px">Get Started</div>
  <div class="btn btn-ghost" style="left:776px;top:446px;width:155px;height:52px">Contact Us</div>
  <div class="arrow-box" style="left:40px;top:344px"><svg viewBox="0 0 16 16"><path d="M10 3L5 8l5 5"/></svg></div>
  <div class="arrow-box" style="left:1125px;top:344px"><svg viewBox="0 0 16 16"><path d="M6 3l5 5-5 5"/></svg></div>
</section>

<div class="cta-band">
  <p>FAST AND RELIABLE SERVICE FOR YOUR PROJECT OR A QUICK FIX, WE DO IT ALL!</p>
  <div class="btn btn-navy" style="left:899px;top:17px;width:154px;height:52px">Get a Quote</div>
</div>

<div class="about-box">
  <h2 class="section-title">About Us</h2>
  <div class="rule"></div>
  <p>Lorem ipsum dolor sit amet, consectetur adipiscing elit, sed do eiusmod tempor incididunt ut labore et dolore magna aliqua. Ut enim ad minim veniam, quis nostrud exercitation ullamco laboris nisi ut aliquip ex ea commodo consequat. Duis aute irure dolor in reprehenderit in voluptate velit esse cillum</p>
  <div class="btn btn-navy" style="left:66px;top:338px;width:154px;height:52px">Read More</div>
</div>
<div class="photo" style="left:653px;top:956px;width:474px;height:436px;background:linear-gradient(160deg,#c7d3dc 0%,#e6e2d2 40%,#b9c86a 75%,#6a7a45 100%);box-shadow:0 3px 8px rgba(0,0,0,.2)" role="img" aria-label="Two site engineers in hard hats and hi-vis vests pointing across a building site"></div>

<section class="projects">
  <div class="ghost">PROJECTS</div>
  <h2>PROJECTS</h2>
  <div class="btn btn-orange" style="left:112px;top:284px;width:157px;height:54px">Next</div>
  <div class="btn" style="left:113px;top:355px;width:156px;height:53px;border:1px solid #fff;color:#fff">Prev</div>

  <div class="card" style="left:301px">
    <div class="photo" style="background:linear-gradient(160deg,#bcd3e8,#cfa68a 55%,#7a6a5a)" role="img" aria-label="Worker in hard hat reviewing plans beside a timber frame house"></div>
    <div class="cat">CONSTRUCTION</div>
    <h3>Lorem ipsum dolor sit amet</h3>
    <p>Lorem ipsum dolor sit amet, consectetur adipiscing<br>elit, sed do eiusmod tempor incididunt ut labore</p>
    <div class="find">Find Out More</div>
  </div>
  <div class="card" style="left:631px">
    <div class="photo" style="background:linear-gradient(160deg,#e8e4dc,#c9b79a 50%,#8d7a5e)" role="img" aria-label="Engineer with blueprints inside a building frame with scaffolding"></div>
    <div class="cat">DEVELOPMENT</div>
    <h3>Lorem ipsum dolor sit amet</h3>
    <p>Lorem ipsum dolor sit amet, consectetur adipiscing<br>elit, sed do eiusmod tempor incididunt ut labore</p>
    <div class="find">Find Out More</div>
  </div>
  <div class="card" style="left:958px">
    <div class="photo" style="background:linear-gradient(180deg,#a9c4d8,#8a8880 55%,#5e5a52)" role="img" aria-label="High-rise tower under construction with a crane"></div>
    <div class="cat">CONSTRUCTION</div>
    <h3>Lorem ipsum dolor sit amet</h3>
    <p>Lorem ipsum dolor sit amet, consectetur adipiscing<br>elit, sed do eiusmod tempor incididunt ut labore</p>
    <div class="find">Find Out More</div>
  </div>
</section>

<section class="offer">
  <div class="photo" style="left:113px;top:2303px;width:458px;height:400px;background:linear-gradient(180deg,#f3a43c 0%,#e8862a 45%,#5a3a1e 80%,#1e1712 100%);box-shadow:0 3px 8px rgba(0,0,0,.2)" role="img" aria-label="Silhouettes of construction workers and a tower crane at sunset"></div>
  <h2>What We Offer</h2>
  <p style="top:2382px">Lorem ipsum dolor sit amet, consectetur adipiscing elit, sed do eiusmod tempor incididunt ut labore et dolore magna aliqua. Ut enim ad minim veniam, quis nostrud</p>
  <p style="top:2461px">Lorem ipsum dolor sit amet, consectetur adipiscing elit, sed do eiusmod tempor incididunt ut labore et dolore magna aliqua. Ut enim ad minim veniam, quis nostrud</p>
  <p style="top:2540px">Lorem ipsum dolor sit amet, consectetur adipiscing elit, sed do eiusmod tempor incididunt ut labore et dolore magna aliqua. Ut enim ad minim veniam, quis nostrud</p>
  <div class="btn btn-orange" style="left:616px;top:2625px;width:155px;height:52px">Read More</div>
  <div class="tab">CONSTRUCTION</div>
  <div class="arrow-box arrow-line" style="left:1156px;top:2367px;width:44px;height:48px"><svg viewBox="0 0 16 16"><path d="M10 3L5 8l5 5"/></svg></div>
</section>

<section class="testi">
  <h2 class="section-title">Testimonials</h2>
  <div class="quote" style="left:28px;top:20px">&ldquo;</div>
  <div class="quote" style="left:1068px;top:265px">&rdquo;</div>
  <div class="tcard dark" style="left:162px">
    <div class="avatar" role="img" aria-label="Client portrait"></div>
    <div class="name">Dana Whitfield</div>
    <div class="role">Lorem ipsum dolor</div>
    <p>Lorem ipsum dolor sit amet, consectetur adipiscing elit, sed do eiusmod tempor incididunt ut labore et dolore magna aliqua. Ut enim ad minim veniam, quis nostrud exercitation ullamco laboris</p>
  </div>
  <div class="tcard light" style="left:610px">
    <div class="avatar" role="img" aria-label="Client portrait"></div>
    <div class="name">Dana Whitfield</div>
    <div class="role">Lorem ipsum dolor</div>
    <p>Lorem ipsum dolor sit amet, consectetur adipiscing elit, sed do eiusmod tempor incididunt ut labore et dolore magna aliqua. Ut enim ad minim veniam, quis nostrud exercitation ullamco laboris</p>
  </div>
  <div class="dots"><span></span><span></span><span class="on"></span><span></span><span></span></div>
</section>

<footer class="footer">
  <h4 class="small" style="left:113px;top:74px">R &amp; M Group Developments Limited</h4>
  <div class="txt" style="left:113px;top:112px;width:320px;font-size:11.5px">Lorem ipsum dolor sit amet, consectetur adipiscing elit, sed do eiusmod tempor incididunt ut labore et dolore magna aliqua. Ut enim ad minim veniam, quis nostrud exercitation ullamco laboris nisi ut aliquip ex ea commodo</div>

  <h4 style="left:482px">Our Services</h4>
  <div class="txt" style="left:482px;top:112px;font-size:13px;line-height:32px">Construction<br>Development</div>

  <h4 style="left:655px">Office in &nbsp;Halifax</h4>
  <div class="txt" style="left:655px;top:112px">
    <div class="row"><svg viewBox="0 0 10 12"><path d="M5 0a4 4 0 0 1 4 4c0 3-4 8-4 8S1 7 1 4a4 4 0 0 1 4-4z"/></svg>48 Halifax, Nova Scotia</div>
    <div class="row"><svg viewBox="0 0 12 12"><path d="M2.5 1l2 .3.8 2.2-1.2 1a7 7 0 0 0 3.4 3.4l1-1.2 2.2.8.3 2c-.2.8-1 1.3-1.8 1.3A9 9 0 0 1 1 2.8C1 2 1.6 1.2 2.5 1z"/></svg>902-555-0148</div>
    <div class="row"><svg viewBox="0 0 12 12"><rect x="1" y="2.5" width="10" height="7"/></svg>info@rmgroupdev.ca</div>
  </div>

  <h4 style="left:883px">Our Locations</h4>
  <div class="map-area" role="img" aria-label="Map of the province showing office location pins"></div>
</footer>
<div class="copy">&copy; 2021 All Rights Reserved</div>

</body>
</html>
```